Bold and colurful E-liquid Design Template

I'm looking for a new label for my house range of vape e-liquids. I currently have almost 40 flavours, so I'm looking for a single label design that I can modify to create the rest of the flavours.
Each label will have the same design, but I'll change the color for each flavour and the name.
I'd like the label to be predominantly text based with bold text and bold colours. I like bold typographic styles. Also for each flavour I'd like to add 1 - 3 letters to represent the flavour. This can be in a larger font.
eg for
Blueberry I'll use the letter B
Pineapple Peach will use PP
Cinnamon Blueberry Muffin uses CBM
The colour used on the label will also be important so they stand out nicely on the shelf.
I've attached a psd mockup of the bottles I'll be using.

```html
<!DOCTYPE html>
<html lang="en">
<head>
<meta charset="utf-8">
<title>Pineapple Peach E-Liquid Label</title>
<link rel="stylesheet" href="https://fonts.googleapis.com/css2?family=Montserrat:wght@400;600;700;800;900&display=swap">
<style>
  :root {
    --flavour: #c35a2c;
    --flavour-deep: #b14a1e;
    --ink: #111111;
    --label: #ffffff;
    --backdrop: #e4e5e5;
  }
  * { margin: 0; padding: 0; box-sizing: border-box; }
  html, body {
    width: 1037px;
    height: 1200px;
    overflow: hidden;
    background: var(--backdrop);
    font-family: "Montserrat", sans-serif;
  }
  .label {
    position: absolute;
    left: 333px;
    top: 45px;
    width: 371px;
    height: 1111px;
    background: var(--label);
    overflow: hidden;
    color: var(--ink);
    text-align: center;
  }
  .label-band {
    position: absolute;
    left: 0;
    width: 100%;
    background: var(--flavour-deep);
  }
  .label-band--top { top: 0; height: 48px; }
  .label-band--bottom { bottom: 0; height: 57px; }
  .brand-tag {
    position: absolute;
    top: 103px;
    left: 68px;
    width: 240px;
    height: 85px;
    background: var(--ink);
    color: #ffffff;
    font-weight: 400;
    font-size: 35px;
    line-height: 85px;
    letter-spacing: 0;
    white-space: nowrap;
  }
  .flavour-code {
    position: absolute;
    top: 218px;
    left: 0;
    width: 100%;
    font-weight: 900;
    font-size: 236px;
    line-height: 1;
    letter-spacing: -10px;
    color: var(--flavour);
  }
  .flavour-name {
    position: absolute;
    top: 462px;
    left: 0;
    width: 100%;
    font-weight: 900;
    font-size: 62px;
    line-height: 74px;
    letter-spacing: -3px;
    text-transform: uppercase;
    white-space: nowrap;
  }
  .product-type {
    position: absolute;
    top: 670px;
    left: 38px;
    width: 297px;
    height: 109px;
    background: var(--flavour);
    color: #ffffff;
    font-weight: 800;
    font-size: 46px;
    line-height: 109px;
    letter-spacing: 3px;
  }
  .strength {
    position: absolute;
    top: 824px;
    left: 0;
    width: 100%;
    font-weight: 600;
    font-size: 36px;
    line-height: 52px;
  }
  .divider {
    position: absolute;
    top: 900px;
    left: 46px;
    width: 283px;
    height: 4px;
    background: var(--flavour);
  }
  .volume {
    position: absolute;
    top: 948px;
    left: 0;
    width: 100%;
    font-weight: 800;
    font-size: 56px;
    line-height: 70px;
  }
</style>
</head>
<body>
  <main class="label">
    <div class="label-band label-band--top"></div>
    <div class="brand-tag">MAREVALE</div>
    <div class="flavour-code">PP</div>
    <h1 class="flavour-name">Pineapple<br>Peach</h1>
    <div class="product-type">E-LIQUID</div>
    <p class="strength">70mg / 30ml</p>
    <div class="divider"></div>
    <p class="volume">60ml</p>
    <div class="label-band label-band--bottom"></div>
  </main>
</body>
</html>
```